Mandarin tuition, language and travel services

We need a website for a new startup company, which offers Mandarin tuition, translating and interpreting, and travel services. Our company is based in Jersey, a British channel island. We would like a creative and modern professional website. Preferably with some animations. The attached is a website, which style we would prefer:
http://www.morvaliqa.com/
We have also attached our logo for your reference
We would also like to see designs using black, red and orange, which corresponds with our logo colours. The cartoon images could be travel resorts in China, and the president of China waving to the web-browsers. Of course, we wouldn't wish to restrain the designers creativity. Any creative and interesting ideas are welcomed! We look forward to hearing from you!

Target Market(s)

school children and adults

Industry/Entity Type

It Company

Number of Pages Required

3 page

Requirements
Must have
• We would prefer a small 3 pages website, if possible. The 3 pages need to be Services, News Room, and Contact us.

```html
<!DOCTYPE html>
<html lang="en">
<head>
<meta charset="utf-8">
<title>Lanqiao Mandarin</title>
<link href="https://fonts.googleapis.com/css2?family=Fira+Sans:wght@300;400;500&family=Josefin+Sans:wght@300&display=swap" rel="stylesheet">
<style>
  :root {
    --black: #000000;
    --charcoal: #1b1b1d;
    --red: #d0181f;
    --title-red: #d3141c;
    --white: #ffffff;
    --body-text: #c9c9c9;
    --frame: #e6e6e6;
  }
  * { margin: 0; padding: 0; box-sizing: border-box; }
  html, body { width: 1026px; height: 1200px; overflow: hidden; }
  body { font-family: "Fira Sans", sans-serif; background: var(--black); color: var(--white); position: relative; }

  .site-header { position: absolute; top: 0; left: 0; width: 1026px; height: 145px; background: var(--black); }
  .social-links { position: absolute; left: 63px; top: 42px; display: flex; gap: 4px; }
  .social-links span { width: 24px; height: 24px; border: 1.5px solid var(--white); border-radius: 50%; display: block; }
  .brand { position: absolute; left: 0; width: 1026px; top: 40px; display: flex; justify-content: center; align-items: center; gap: 8px; }
  .brand-dot { width: 18px; height: 18px; border-radius: 50%; background: var(--red); }
  .brand-name { font-weight: 500; font-size: 24px; color: var(--white); letter-spacing: 0.5px; }
  .call-box { position: absolute; left: 836px; top: 38px; display: flex; gap: 8px; align-items: flex-start; }
  .call-box svg { margin-top: 4px; }
  .call-label { font-size: 12px; font-weight: 300; line-height: 14px; }
  .call-number { font-size: 15px; font-weight: 500; line-height: 20px; }
  .main-nav { position: absolute; top: 112px; left: 0; width: 1026px; display: flex; justify-content: center; gap: 41px; font-size: 14px; font-weight: 400; padding-left: 8px; }

  .hero { position: absolute; top: 145px; left: 0; width: 1026px; height: 474px;
    background: linear-gradient(180deg, #c9cfc9 0%, #8aa07e 22%, #4d7a3c 45%, #b5562f 62%, #3d6a2c 78%, #9c2a2a 92%, #3a5a28 100%); }

  .welcome { position: absolute; top: 619px; left: 0; width: 1026px; height: 480px; background: var(--charcoal); }
  .welcome-frame { position: absolute; top: 0; left: 0; }
  .welcome-kicker { position: absolute; top: 116px; width: 100%; text-align: center; font-family: "Josefin Sans", sans-serif; font-weight: 300; font-size: 25px; letter-spacing: 1px; color: var(--white); }
  .welcome-title { position: absolute; top: 142px; width: 100%; text-align: center; font-family: "Josefin Sans", sans-serif; font-weight: 300; font-size: 37px; color: var(--title-red); }
  .welcome-text { position: absolute; top: 203px; left: 140px; width: 746px; text-align: center; font-size: 14px; font-weight: 300; line-height: 23.7px; color: var(--body-text); }

  .site-footer { position: absolute; top: 1099px; left: 0; width: 1026px; height: 101px; background: var(--red); font-size: 12.5px; line-height: 17.5px; font-weight: 400; }
  .footer-item { position: absolute; top: 32px; display: flex; gap: 8px; align-items: flex-start; }
  .footer-divider { position: absolute; left: 690px; top: 32px; width: 1px; height: 34px; background: rgba(255,255,255,0.35); }
  .footer-legal { position: absolute; right: 63px; top: 32px; text-align: right; }
</style>
</head>
<body>
  <header class="site-header">
    <div class="social-links" aria-label="Social links"><span></span><span></span><span></span><span></span><span></span></div>
    <div class="brand"><span class="brand-dot"></span><span class="brand-name">Lanqiao Mandarin</span></div>
    <div class="call-box">
      <svg width="20" height="20" viewBox="0 0 24 24" fill="none" stroke="#fff" stroke-width="1.4"><path d="M5 3l4 1 1.5 4-2.5 2a12 12 0 0 0 6 6l2-2.5 4 1.5 1 4-2 2C11 21 3 13 3 5z"/></svg>
      <div><div class="call-label">Call Us Today</div><div class="call-number">1800 555 0142</div></div>
    </div>
    <nav class="main-nav"><span>HOME</span><span>ABOUT US</span><span>SERVICES</span><span>NEWS ROOM</span><span>CONTACT US</span></nav>
  </header>

  <div class="hero" role="img" aria-label="Aerial view of a traditional Chinese palace complex with orange roofs among green trees"></div>

  <section class="welcome">
    <svg class="welcome-frame" width="1026" height="480" viewBox="0 0 1026 480" fill="none" stroke="var(--frame)" stroke-width="1">
      <rect x="95" y="61" width="837" height="364"/>
      <rect x="91" y="57" width="845" height="372"/>
    </svg>
    <div class="welcome-kicker">WELCOME TO</div>
    <div class="welcome-title">LANQIAO MANDARIN</div>
    <p class="welcome-text">Duis autem vel eum iriure dolor in hendrerit in vulputate velit esse molestie consequat, vel illum dolore eu feugiat nulla facilisis at vero eros et accumsan et iusto odio dignissim qui blandit praesent luptatum zzril delenit augue duis dolore te feugait nulla facilisi. Nam liber tempor cum soluta nobis eleifend option congue nihil imperdiet doming id quod mazim placerat facer possim assum. Typi non habent claritatem insitam; est usus legentis in iis qui facit eorum facilisi. Nam liber tempor cum soluta nobis eleifend option congue nihil imperdiet doming id quod mazim placerat facer possim assum. Typi non habent claritatem insitam; est usus legentis in iis qui facit eorum claritatem. Investigationes demonstraverunt lectores legere me lius quod ii legunt saepius.</p>
  </section>

  <footer class="site-footer">
    <div class="footer-item" style="left:63px">
      <svg width="18" height="26" viewBox="0 0 18 26" fill="none" stroke="#fff" stroke-width="1.2"><path d="M9 25S1 14 1 9a8 8 0 0 1 16 0c0 5-8 16-8 16z"/><circle cx="9" cy="9" r="3"/></svg>
      <div>228 loremipsum dolor sit,<br>dosis amet 858585</div>
    </div>
    <div class="footer-item" style="left:294px">
      <svg width="22" height="22" viewBox="0 0 24 24" fill="none" stroke="#fff" stroke-width="1.3"><path d="M5 3l4 1 1.5 4-2.5 2a12 12 0 0 0 6 6l2-2.5 4 1.5 1 4-2 2C11 21 3 13 3 5z"/></svg>
      <div>Call Us:<br>1800 555 0142</div>
    </div>
    <div class="footer-item" style="left:465px">
      <svg width="28" height="22" viewBox="0 0 28 22" fill="none" stroke="#fff" stroke-width="1.2"><path d="M8 6l18-4-4 16-14 0z"/><path d="M8 6l9 6 9-10"/><path d="M1 11h5M2 14h5M3 17h5"/></svg>
      <div>Email Us:<br>info@lanqiaomandarin.com</div>
    </div>
    <div class="footer-divider"></div>
    <div class="footer-legal">©2016 Lanqiao Mandarin All Rights Reserved<br>Terms of Use | Privacy Policy | Sitemap</div>
  </footer>
</body>
</html>
```